Arabic Alphabet Art Contest

Arabic Studies at Brimwood

Arabic Art Contest

Express yourselves through Arabic Art

Calling all student artists to participate in Brimwood's 1st Arabic Art Contest

The Arabic Alphabet is made up of 28 letters. Let's see you artistic skills by creating a poster with all of the Arabic Alphabets

Art Submissions due by: February 1st, 2021
Submit all entries to Mr. Tovelin

Grade Prize: $100 Quillmart Gift Card
Second Prize: $75 Quillmart Gift Card
3rd Prize: $50 Quillmart Gift Card
4th Prize: $25 Gift Card

```html
<!DOCTYPE html>
<html lang="en">
<head>
<meta charset="UTF-8">
<title>Arabic Alphabet Art Contest</title>
<link href="https://fonts.googleapis.com/css2?family=Montserrat:wght@700;800&family=Cormorant+Garamond:wght@500&family=Libre+Caslon+Text&family=Yellowtail&display=swap" rel="stylesheet">
<style>
  :root{
    --saffron:#f7b538;
    --ember:#da5a3a;
    --ink:#141414;
    --teal:#2a7f96;
    --mist:#a9b6c2;
    --paper:#ffffff;
  }
  html,body{margin:0;padding:0;overflow:hidden;}
  body{width:849px;height:1200px;}
  .poster{position:relative;width:849px;height:1200px;background:var(--saffron);overflow:hidden;font-family:"Montserrat",Arial,sans-serif;color:var(--ink);}
  .letter-column{position:absolute;left:0;top:0;width:212px;height:1200px;
    background:linear-gradient(160deg,var(--ember) 0%,var(--saffron) 18%,var(--teal) 34%,var(--saffron) 48%,var(--ink) 60%,var(--saffron) 72%,var(--mist) 84%,var(--ember) 100%);
    opacity:.55;}
  .centered{position:absolute;left:212px;right:0;text-align:center;}
  .kicker{top:58px;font-weight:700;font-size:19px;}
  .title{top:102px;font-family:"Cormorant Garamond",Georgia,serif;font-weight:500;font-size:62px;line-height:1;margin:0;left:190px;}
  .brush{position:absolute;left:188px;top:168px;width:612px;height:190px;}
  .tagline{position:absolute;left:200px;top:190px;width:590px;transform:rotate(-7deg);text-align:center;
    font-family:"Yellowtail",cursive;font-size:54px;line-height:1.05;color:var(--paper);
    -webkit-text-stroke:1.5px var(--ember);letter-spacing:2px;}
  .call{top:370px;font-weight:800;font-size:26px;line-height:35px;margin:0;}
  .lede{top:498px;font-family:"Libre Caslon Text",Georgia,serif;font-size:20px;line-height:32px;margin:0;}
  .due-label{top:628px;font-weight:800;font-size:20px;}
  .due-date{top:654px;font-weight:800;font-size:31px;}
  .submit{top:692px;font-weight:800;font-size:19px;}
  .submit .name{background:var(--ember);color:var(--paper);padding:1px 5px;}
  .prize{position:absolute;width:230px;height:180px;text-align:center;color:var(--paper);}
  .prize svg{position:absolute;left:0;top:0;}
  .prize .rank{position:relative;display:block;padding-top:48px;font-weight:700;font-size:19px;}
  .prize .amount{position:relative;display:block;font-weight:800;font-size:38px;line-height:42px;}
  .prize .card{position:relative;display:block;font-weight:700;font-size:11.5px;}
  .p1{left:249px;top:738px;} .p2{left:523px;top:738px;}
  .p3{left:249px;top:927px;} .p4{left:523px;top:927px;}
  .school-mark{position:absolute;left:456px;top:1096px;display:flex;align-items:center;gap:6px;font-weight:800;font-size:15px;}
  .school-mark .dot{width:14px;height:14px;border-radius:50%;background:var(--teal);}
  .footer{position:absolute;left:184px;right:0;top:1162px;height:38px;background:var(--ember);display:flex;justify-content:space-around;align-items:center;
    font-family:"Libre Caslon Text",Georgia,serif;font-size:11.5px;letter-spacing:.5px;text-transform:uppercase;color:var(--ink);}
</style>
</head>
<body>
<main class="poster">
  <div class="letter-column" role="img" aria-label="Scattered colourful Arabic letters in black, teal, orange and grey with ink splatters"></div>

  <div class="centered kicker">Arabic Studies at Brimwood</div>
  <h1 class="centered title">Arabic Art Contest</h1>

  <svg class="brush" viewBox="0 0 612 190" aria-hidden="true">
    <polygon points="18,118 120,70 300,40 470,18 600,4 606,34 560,60 590,82 470,110 330,140 160,168 30,186 2,160 40,140" fill="var(--ink)"/>
  </svg>
  <div class="tagline">Express yourselves<br>through Arabic Art</div>

  <p class="centered call">Calling all student artists<br>to participate in Brimwood's 1st<br>Arabic Art Contest</p>

  <p class="centered lede">The Arabic Alphabet is made up of 28 letters.<br>Let's see you artistic skills by creating a poster<br>with all of the Arabic Alphabets</p>

  <div class="centered due-label">Art Submissions due by:</div>
  <div class="centered due-date">February 1st, 2021</div>
  <div class="centered submit">Submit all entries to <span class="name">Mr. Tovelin</span></div>

  <div class="prize p1">
    <svg width="230" height="180" aria-hidden="true"><circle cx="115" cy="90" r="87" fill="var(--ember)"/><polygon points="8,44 222,36 214,150 14,144" fill="var(--ink)"/></svg>
    <span class="rank">GRADE PRIZE</span><span class="amount">$100</span><span class="card">QUILLMART GIFT CARD</span>
  </div>
  <div class="prize p2">
    <svg width="230" height="180" aria-hidden="true"><circle cx="115" cy="90" r="87" fill="var(--ember)"/><polygon points="8,44 222,36 214,150 14,144" fill="var(--ink)"/></svg>
    <span class="rank">SECOND PRIZE</span><span class="amount">$75</span><span class="card">QUILLMART GIFT CARD</span>
  </div>
  <div class="prize p3">
    <svg width="230" height="180" aria-hidden="true"><circle cx="115" cy="90" r="87" fill="var(--ember)"/><polygon points="8,44 222,36 214,150 14,144" fill="var(--ink)"/></svg>
    <span class="rank">3RD PRIZE</span><span class="amount">$50</span><span class="card">QUILLMART GIFT CARD</span>
  </div>
  <div class="prize p4">
    <svg width="230" height="180" aria-hidden="true"><circle cx="115" cy="90" r="87" fill="var(--ember)"/><polygon points="8,44 222,36 214,150 14,144" fill="var(--ink)"/></svg>
    <span class="rank">4TH PRIZE</span><span class="amount">$25</span><span class="card">QUILLMART GIFT CARD</span>
  </div>

  <div class="school-mark"><span class="dot"></span>Brimwood</div>

  <footer class="footer"><span>Arabic Studies at Brimwood</span><span>Arabic Studies at Brimwood</span></footer>
</main>
</body>
</html>
```